High-end Management Consulting Website

I am looking for a design that feels very high end and professional and very serious feeling. I would like a site that uses a lot of white space, with colors in the blue, grey family. You can use a very small about of the orange and green in the logo, but it needs to be a very small amount.

I like images similar to a rock climber helping another one up a mountain. I would love other imagery throughout the site of mountain ranges and people making it to the top.

When you think of the feel imagine people in suites, very corporate feeling. Very much focused on helping company leadership and CEOs solve problems.

From a functionality standpoint https://ninefarthingmoor.com has a good deal of similar content- However, I do not like the colors or the design. I like graphics on websites similar to https://www.bramblecrestholdings.com.

I like clean with lots of white space.

The link below has all of the content and design comments. https://files.quillorbit.com/sheet/d/7KPzXa2LmQ9vTcRw4HbN8sYdE3fUoJ6gZt5VkMnB0wA/view?usp=open

Target Market(s)

High end businesses and very experienced executives.

Industry/Entity Type

Consulting

Coding

Coded - Design and coding required

Number of Pages Required

5+ page

Font styles to use
Sans Serif

Colors

Designer to choose colors to be used in the design.

Requirements
Must have
• white space, blues some gray, clean feel VERY LITTLE use of accent colors.

I want to have a centered navigation bar.
I would like to have a secondary scrolling image.
Nice to have
• High end imagery that speaks to what is being said in the site.
This is not the main image I want to see but I like imagery like this for the main home page.
https://www.pixelharborstock.com/image-photo/couple-hiking-help-each-other-silhouette-917264305
Should not have
• Please do not use dated images or blocky feeling. Please also do not go overboard using the icon in the design.

```html
<!DOCTYPE html>
<html lang="en">
<head>
<meta charset="utf-8">
<title>Keystone Ridge Partners</title>
<link href="https://fonts.googleapis.com/css2?family=Lato:wght@300;400;700;900&family=Roboto:wght@300;400;500&display=swap" rel="stylesheet">
<style>
:root{
  --navy:#1d4a73;
  --navy-deep:#163a5c;
  --blue:#1b8fe0;
  --sky:#5aa9e6;
  --steel:#7f93a8;
  --slate:#5c6d80;
  --grey-mid:#b8c2cc;
  --accent:#f65a07;
  --ink:#2a2a2a;
  --text:#444;
  --pale:#f1f1f1;
  --white:#fff;
}
*{margin:0;padding:0;box-sizing:border-box}
html,body{width:1200px;height:2557px;overflow:hidden;background:var(--white)}
body{position:relative;font-family:'Roboto',sans-serif;color:var(--text)}
.abs{position:absolute}

/* header */
.site-header{position:absolute;left:0;top:0;width:1200px;height:68px;background:var(--white);z-index:5}
.brand{position:absolute;left:196px;top:27px;display:flex;align-items:center;gap:8px}
.brand-mark{width:14px;height:14px;background:var(--navy)}
.brand-name{font-family:'Lato',sans-serif;font-weight:700;font-size:13px;letter-spacing:.5px;color:var(--navy);text-transform:uppercase;line-height:1}
.main-nav{position:absolute;left:0;top:27px;width:1200px;display:flex;justify-content:center;align-items:center;gap:24px;font-family:'Lato',sans-serif;font-weight:700;font-size:9.5px;letter-spacing:.4px;color:#333;line-height:14px}
.nav-cta{position:absolute;right:188px;top:-5px;background:var(--navy);color:var(--white);padding:6px 10px;font-size:8px;font-family:'Lato',sans-serif;font-weight:700;letter-spacing:.4px}

/* hero */
.hero{position:absolute;left:0;top:68px;width:1200px;height:575px;overflow:hidden}
.hero-backdrop{position:absolute;inset:0;background:linear-gradient(120deg,#2c5a86 0%,#1f4c78 45%,#1a4570 100%)}
.hero-photo{position:absolute;left:0;top:0}
.hero-copy{position:absolute;left:196px;top:162px;width:400px;color:var(--white)}
.hero-title{font-family:'Lato',sans-serif;font-weight:900;font-size:31px;line-height:36px;letter-spacing:-.3px}
.hero-sub{font-family:'Lato',sans-serif;font-weight:300;font-size:26px;margin-top:4px}
.hero-text{font-family:'Roboto',sans-serif;font-size:10.4px;line-height:15.3px;margin-top:14px;font-weight:500;width:398px}
.btn-primary{display:inline-block;background:var(--blue);color:var(--white);font-family:'Lato',sans-serif;font-weight:700;font-size:11px;letter-spacing:1px;padding:11px 23px;margin-top:30px}

/* team */
.section-title{font-family:'Lato',sans-serif;font-weight:900;color:var(--ink)}
.team-title{left:0;top:735px;width:1200px;text-align:center;font-size:30px}
.team-intro{left:300px;top:790px;width:600px;text-align:center;font-size:12.6px;line-height:18.6px;color:#444}
.member{position:absolute;top:1114px;width:176px}
.member-role{font-size:12.5px;color:#555;letter-spacing:.3px}
.member-name{font-family:'Lato',sans-serif;font-size:20px;font-weight:700;color:var(--ink);margin-top:2px}
.member-bio{font-size:10.3px;line-height:15.6px;color:#666;margin-top:6px}
.member-link{font-family:'Lato',sans-serif;font-weight:700;font-size:9.5px;color:#222;margin-top:13px}

/* experience */
.experience{position:absolute;left:196px;top:1288px;width:809px;height:172px;display:flex;gap:5px}
.exp-label{width:326px;background:var(--navy);color:var(--white);font-family:'Lato',sans-serif;font-weight:900;font-size:31px;display:flex;align-items:center;justify-content:center;letter-spacing:-.3px}
.exp-client{display:flex;align-items:center;justify-content:center;font-family:'Lato',sans-serif;font-weight:900;color:var(--white);text-align:center}
.client-one{width:173px;background:#ececec;font-size:26px;line-height:28px}
.client-two{width:305px;background:#d2d2d2;font-size:34px}

/* services */
.help-title{left:196px;top:1718px;font-size:52px;line-height:61px;letter-spacing:-.5px}
.service{position:absolute;width:218px;height:200px;background:var(--white);box-shadow:0 2px 10px rgba(0,0,0,.06);display:flex;flex-direction:column;align-items:center;padding-top:28px}
.service-name{font-family:'Lato',sans-serif;font-weight:700;font-size:14.5px;line-height:18px;color:#222;text-align:center;margin-top:14px}

/* contact */
.contact-lead{left:194px;top:2118px;width:380px;font-size:14.3px;line-height:20px;color:#333}
.contact-title{left:196px;top:2190px;font-size:32px;letter-spacing:-.5px}
.contact-form{position:absolute;left:196px;top:2256px;width:369px}
.field{height:52px;border-bottom:3px solid #d9d9d9;font-size:10px;color:#444;padding-top:8px}
.field.message{height:66px}
.btn-submit{margin-top:22px;height:43px;background:linear-gradient(90deg,var(--navy) 50%,var(--blue));color:var(--white);font-family:'Lato',sans-serif;font-weight:700;font-size:13px;letter-spacing:1px;display:flex;align-items:center;justify-content:center}
</style>
</head>
<body>

<header class="site-header">
  <div class="brand"><span class="brand-mark"></span><span class="brand-name">Keystone Ridge Partners</span></div>
  <nav class="main-nav">
    <span>HOME</span><span>ADVISORY SERVICES</span><span>ABOUT</span><span>WORK WITH US</span>
  </nav>
  <span class="nav-cta" style="top:24px">LET'S TALK</span>
</header>

<section class="hero">
  <div class="hero-backdrop" role="img" aria-label="Office desk scene with laptop and documents under a deep blue tint"></div>
  <svg class="hero-photo" width="1200" height="575" viewBox="0 0 1200 575">
    <defs>
      <linearGradient id="teamPhoto" x1="0" y1="0" x2="1" y2="1">
        <stop offset="0" stop-color="#e6e8ea"/>
        <stop offset=".5" stop-color="#c5c9ce"/>
        <stop offset="1" stop-color="#9aa2ab"/>
      </linearGradient>
    </defs>
    <path d="M626 575 L624 130 Q624 68 690 60 L1200 20 L1200 575 Z" fill="url(#teamPhoto)" role="img" aria-label="Three colleagues working together at a laptop"/>
    <path d="M632 298 Q618 320 620 380 L640 575" fill="none" stroke="#5aa9e6" stroke-width="4"/>
  </svg>
  <div class="hero-copy">
    <div class="hero-title">IN TIMES OF ECONOMIC UNCERTAINTY</div>
    <div class="hero-sub">YOU NEED AN EDGE.</div>
    <p class="hero-text">As industry leaders, former company founders, active investors and senior innovation experts, we bring experience, knowledge and connections to our engagements. Leading to cost and time savings, higher opportunity utilization and better business outcomes.</p>
    <span class="btn-primary">LEARN MORE</span>
  </div>
</section>

<svg class="abs" style="left:0;top:643px" width="1200" height="660" viewBox="0 0 1200 660">
  <polygon points="736,20 780,92 696,92" fill="#f2f2f2"/>
  <polygon points="830,130 1200,60 1200,200 860,190" fill="#f6f6f6"/>
  <polygon points="90,135 300,180 150,470 0,470 0,260" fill="#f6f6f6"/>
  <polygon points="196,468 150,540 196,540" fill="#ededed"/>
  <polygon points="990,340 1200,400 1200,500 1068,640" fill="#f0f0f0"/>
  <path d="M428 376 Q450 386 468 378 M462 372 L468 378 L460 382" fill="none" stroke="#b5b5b5" stroke-width="1.5"/>
  <path d="M735 380 Q755 366 778 372 M770 366 L778 372 L770 376" fill="none" stroke="#b5b5b5" stroke-width="1.5"/>
  <defs>
    <linearGradient id="portrait" x1="0" y1="0" x2="0" y2="1">
      <stop offset="0" stop-color="#e2e2e2"/><stop offset="1" stop-color="#8f9398"/>
    </linearGradient>
  </defs>
  <path d="M270 278 Q350 262 380 330 Q395 420 345 458 Q270 470 215 430 Q185 380 210 330 Q230 288 270 278Z" fill="url(#portrait)" role="img" aria-label="Portrait of the chief executive"/>
  <circle cx="238" cy="305" r="30" fill="#7f93a8"/>
  <path d="M570 272 Q650 270 685 340 Q700 420 640 462 Q560 475 520 430 Q495 380 510 320 Q530 275 570 272Z" fill="url(#portrait)" role="img" aria-label="Portrait of the HR manager"/>
  <circle cx="660" cy="426" r="28" fill="#1d4a73"/>
  <path d="M900 274 Q985 265 1002 330 Q1010 420 955 460 Q880 472 842 440 Q812 400 820 340 Q845 282 900 274Z" fill="url(#portrait)" role="img" aria-label="Portrait of the HR senior executive"/>
  <circle cx="866" cy="436" r="25" fill="#1b8fe0"/>
</svg>

<h2 class="abs section-title team-title">OUR TEAM</h2>
<p class="abs team-intro">Our partners have served in executive leadership for fortune 1000 global organizations, served at the highest levels of office and managed billions in buy and sell side transactions. Our experience, founding, scaling, exiting and acquiring companies along the way, gives our team a unique understanding of the clients we serve.</p>

<div class="member" style="left:200px">
  <div class="member-role">CHIEF EXECUTIVE</div>
  <div class="member-name">Nora Whitfield</div>
  <div class="member-bio">Ignobly belched incoherently poetic enticing cowered where grateful hatchet resold ferret.</div>
  <div class="member-link">FIND OUT MORE &rsaquo;</div>
</div>
<div class="member" style="left:512px">
  <div class="member-role">HR MANAGER</div>
  <div class="member-name">Claire Dumont</div>
  <div class="member-bio">Ignobly belched incoherently poetic enticing cowered where grateful hatchet resold ferret.</div>
  <div class="member-link">FIND OUT MORE &rsaquo;</div>
</div>
<div class="member" style="left:816px">
  <div class="member-role">HR SENIOR EXECUTIVE</div>
  <div class="member-name">Julian Reyes</div>
  <div class="member-bio">Ignobly belched incoherently poetic enticing cowered where grateful hatchet resold ferret.</div>
  <div class="member-link">FIND OUT MORE &rsaquo;</div>
</div>

<section class="experience">
  <div class="exp-label">OUR EXPERIENCE</div>
  <div class="exp-client client-one">Harrowgate Capital</div>
  <div class="exp-client client-two">Northlight Summit</div>
</section>

<svg class="abs" style="left:0;top:1580px" width="1200" height="977" viewBox="0 0 1200 977">
  <polygon points="1048,5 1200,70 1200,380 1085,335" fill="#1b8fe0"/>
  <polygon points="1085,335 1200,250 1200,380" fill="#3a9fe8"/>
  <polygon points="820,550 1085,335 1200,380 1200,520 1120,665" fill="#1d4a73"/>
  <polygon points="1085,335 1200,380 1200,520" fill="#2c5d8c"/>
  <polygon points="919,90 958,68 980,280 919,330" fill="#b8c2cc"/>
  <polygon points="919,270 980,280 919,330" fill="#7f93a8"/>
  <rect x="688" y="38" width="13" height="167" fill="#1b8fe0"/>
  <rect x="688" y="220" width="13" height="150" fill="#1d4a73"/>
  <rect x="701" y="205" width="190" height="15" fill="#5aa9e6"/>
  <polygon points="505,205 630,205 622,217 512,217" fill="#7f93a8"/>
  <polygon points="0,625 160,940 130,977 0,977" fill="#1b8fe0"/>
</svg>

<h2 class="abs section-title help-title">HOW<br>WE HELP</h2>

<div class="service" style="left:470px;top:1585px">
  <svg width="72" height="72" viewBox="0 0 72 72" fill="none" stroke="#1b8fe0" stroke-width="2.2">
    <rect x="28" y="4" width="40" height="40" rx="2"/><line x1="34" y1="14" x2="62" y2="14"/><line x1="34" y1="24" x2="62" y2="24"/><line x1="34" y1="34" x2="62" y2="34"/>
    <circle cx="20" cy="32" r="9"/><path d="M4 70 V56 Q4 44 20 44 Q36 44 36 56 V70Z"/><path d="M20 44 L17 58 L20 64 L23 58Z"/>
  </svg>
  <div class="service-name">Executive<br>Advisory Services</div>
</div>
<div class="service" style="left:701px;top:1585px">
  <svg width="72" height="72" viewBox="0 0 72 72" fill="none" stroke="#1d4a73" stroke-width="2.2">
    <rect x="4" y="4" width="54" height="64"/><rect x="12" y="16" width="14" height="10"/><rect x="12" y="34" width="14" height="10"/><rect x="36" y="12" width="14" height="10"/><rect x="36" y="28" width="14" height="10"/><rect x="36" y="46" width="14" height="10"/>
    <path d="M26 21 H31 V51 H36 M31 33 H36 M31 17 H36"/><path d="M64 14 V62 L62 68 L60 62 V14Z"/>
  </svg>
  <div class="service-name">Business Model Design<br>&amp; Implementation</div>
</div>
<div class="service" style="left:470px;top:1800px">
  <svg width="72" height="72" viewBox="0 0 72 72" fill="none" stroke="#5c6d80" stroke-width="2.2">
    <rect x="4" y="4" width="64" height="64"/><line x1="4" y1="14" x2="68" y2="14"/><rect x="12" y="22" width="48" height="12"/><line x1="12" y1="42" x2="40" y2="42"/><line x1="12" y1="50" x2="40" y2="50"/><line x1="12" y1="58" x2="40" y2="58"/><rect x="46" y="42" width="14" height="18"/>
  </svg>
  <div class="service-name">Turnaround and<br>Restructuring</div>
</div>
<div class="service" style="left:701px;top:1800px">
  <svg width="72" height="72" viewBox="0 0 72 72" fill="none" stroke="#555" stroke-width="2">
    <circle cx="36" cy="36" r="32"/><circle cx="36" cy="36" r="22"/><circle cx="36" cy="36" r="12"/>
    <path d="M40 30 Q36 27 32 30 Q31 35 36 36 Q41 37 40 42 Q36 45 32 42 M36 26 V46"/>
  </svg>
  <div class="service-name">Revenue<br>Enhancement</div>
</div>

<p class="abs contact-lead">Global experience. Local market expertise. Our network of international business C-Suite executives represents every major business sector.</p>
<h2 class="abs section-title contact-title">READY TO LEARN MORE?</h2>
<form class="contact-form">
  <div class="field">Your Name</div>
  <div class="field">Your Email Address</div>
  <div class="field message">Your Message</div>
  <div class="btn-submit">SUBMIT NOW</div>
</form>

<svg class="abs" style="left:610px;top:2100px" width="480" height="420" viewBox="0 0 480 420">
  <g transform="rotate(-3 240 210)">
    <path d="M60 40 H400 Q450 40 450 90 V340 Q450 380 410 385" fill="none" stroke="#1d4a73" stroke-width="3"/>
    <rect x="22" y="28" width="420" height="360" rx="34" fill="#f5f5f5" stroke="#e0e0e0" role="img" aria-label="Street map showing the office location"/>
  </g>
</svg>

</body>
</html>
```